Wine Label for a Prosecco Wine Called Vuro

Prosecco is a white sparkling wine from Italy. We are looking for an eye catching, elegant label for this prosecco that is called "Vuro" because it is a young, fresh, lively white sparkling wine. (We do not want to see children or babies featured on the label-- just the name VURO please.) Attached is the old label for your reference, and the bottle type that will be used , which is a dark green Burgundy style bottle (pls ignore the label on the bottle). Please no grapes or wine glasses on the label. We are looking for something: eye catching / fun / ELEGANT (not cheap). We would be happy with a fun color too. Remember-- elegant, eye catching! Thanks!
Updates

Hi All, I think I made a mistake in my brief and have updated it. I also uploaded a competitor's label that we like very much to give better direction to what we are looking for. Also, the word Vuro cannot be vertical, nor can it be broken. It needs to read: VURO or Vuro. Thanks

Target Market(s)

American adults male and female.

Colors
abd036
33a6d7
33b8a4
ffcf3e

Requirements
Must have
• The mandatory information as shown on old labels. The word VURO should be very prominent.
Nice to have
• The uploaded photo of a competitor's prosecco shows a label we really like... if you could play around with this shape and style we'd be very happy.
Should not have
• No grape images, no wine glass images, no images of babies or children.

```html
<!DOCTYPE html>
<html lang="it">
<head>
<meta charset="utf-8">
<title>Vuro Prosecco – Label Variants</title>
<link rel="stylesheet" href="https://fonts.googleapis.com/css2?family=Playfair+Display:wght@400&display=swap">
<style>
  :root {
    --plum: #3b1940;
    --gold: #c49f4a;
    --white: #ffffff;
    --page: #ffffff;
    --edge: #d9d9d9;
  }
  * { margin: 0; padding: 0; box-sizing: border-box; }
  html, body {
    width: 923px;
    height: 1200px;
    overflow: hidden;
    background: var(--page);
  }
  .sheet {
    position: relative;
    width: 923px;
    height: 1200px;
    display: flex;
    justify-content: center;
    align-items: center;
    gap: 30px;
  }
  .label {
    position: relative;
    width: 420px;
    height: 330px;
  }
  .label__shape {
    position: absolute;
    inset: 0;
    width: 100%;
    height: 100%;
  }
  .label__content {
    position: absolute;
    inset: 0;
    text-align: center;
    font-family: "Playfair Display", serif;
    font-weight: 400;
  }
  .label__ornament {
    position: absolute;
    left: 50%;
    top: 34px;
    width: 150px;
    height: 50px;
    transform: translateX(-50%);
    border-radius: 40% 40% 10% 10%;
  }
  .label__name {
    position: absolute;
    left: 0;
    right: 0;
    top: 96px;
    font-size: 62px;
    font-weight: 400;
    line-height: 1;
    letter-spacing: 6px;
    padding-left: 6px;
    color: var(--white);
  }
  .label__type {
    position: absolute;
    left: 0;
    right: 0;
    top: 170px;
    font-size: 22px;
    line-height: 1;
    letter-spacing: 4px;
    padding-left: 4px;
  }
  .label__region {
    position: absolute;
    left: 0;
    right: 0;
    top: 216px;
    font-size: 18px;
    line-height: 1;
    letter-spacing: 1px;
    color: var(--white);
  }
  .label__rule {
    position: absolute;
    left: 50%;
    top: 245px;
    width: 40px;
    height: 1px;
    transform: translateX(-50%);
  }
  .label__appellation,
  .label__style {
    position: absolute;
    left: 0;
    right: 0;
    font-size: 10px;
    line-height: 1;
    color: var(--white);
  }
  .label__appellation { top: 258px; }
  .label__style { top: 276px; letter-spacing: 0.5px; }

  .label--plum .label__ornament { background: var(--gold); opacity: 0.55; }
  .label--plum .label__type { color: var(--gold); }
  .label--plum .label__rule { background: var(--gold); }

  .label--gold .label__ornament { background: var(--plum); opacity: 0.45; }
  .label--gold .label__type { color: var(--plum); }
  .label--gold .label__rule { background: var(--plum); }
</style>
</head>
<body>
<main class="sheet">

  <section class="label label--plum">
    <svg class="label__shape" viewBox="0 0 470 370" preserveAspectRatio="none" aria-hidden="true">
      <path d="M6 96 C60 91 110 72 140 46 C180 10 290 10 330 46 C360 72 410 91 464 96 L464 296 C410 301 360 320 330 340 C290 366 180 366 140 340 C110 320 60 301 6 296 Z"
            fill="var(--plum)" stroke="var(--gold)" stroke-width="5"/>
    </svg>
    <div class="label__content">
      <div class="label__ornament" role="img" aria-label="Gold flourish ornament"></div>
      <h1 class="label__name">VURO</h1>
      <p class="label__type">PROSECCO</p>
      <p class="label__region">VENETO</p>
      <span class="label__rule"></span>
      <p class="label__appellation">Indicazione Geografica Tipica</p>
      <p class="label__style">FRIZZANTE</p>
    </div>
  </section>

  <section class="label label--gold">
    <svg class="label__shape" viewBox="0 0 470 370" preserveAspectRatio="none" aria-hidden="true">
      <path d="M6 96 C60 91 110 72 140 46 C180 10 290 10 330 46 C360 72 410 91 464 96 L464 296 C410 301 360 320 330 340 C290 366 180 366 140 340 C110 320 60 301 6 296 Z"
            fill="var(--gold)" stroke="var(--edge)" stroke-width="7"/>
      <path d="M6 96 C60 91 110 72 140 46 C180 10 290 10 330 46 C360 72 410 91 464 96 L464 296 C410 301 360 320 330 340 C290 366 180 366 140 340 C110 320 60 301 6 296 Z"
            fill="none" stroke="var(--white)" stroke-width="5"/>
    </svg>
    <div class="label__content">
      <div class="label__ornament" role="img" aria-label="Plum flourish ornament"></div>
      <h1 class="label__name">VURO</h1>
      <p class="label__type">PROSECCO</p>
      <p class="label__region">VENETO</p>
      <span class="label__rule"></span>
      <p class="label__appellation">Indicazione Geografica Tipica</p>
      <p class="label__style">FRIZZANTE</p>
    </div>
  </section>

</main>
</body>
</html>
```